Short Stage Works Gathering

I need a poster design for our 2012 play festival called 'The Harlow Bay Gathering of Short Stage Works 2012'. We are a community theatre in Port Macquarie, NSW, Australia. A beautiful seaside town with Norfolk Pine Trees and lots of pelicans. Our website is at www.curtaincallstage.org.au for more info. Our logo colours are a vibrant navy blue, red and yellow. The poster would need to depict drama, theatre, our logo, fun, and excitement. The dates are 8 - 10 June 2012. For more information e-mail r.m.dunwell@tidemail.com

Target Market(s)

All age groups and people interested in theatre

Industry/Entity Type

Festival

Requirements
Must have
• Title - Harlow Bay Gathering of Short Stage Works
For more information e-mail r.m.dunwell@tidemail.com
Dates - 8 - 10 June 2012
Curtain Call Stage Logo
Website Address - www.curtaincallstage.org.au
Nice to have
• Background could include a picture of a theatrical stage

```html
<!DOCTYPE html>
<html lang="en">
<head>
<meta charset="utf-8">
<title>Harlow Bay Gathering of Short Stage Works 2012</title>
<link rel="stylesheet" href="https://fonts.googleapis.com/css2?family=Bebas+Neue&family=Yesteryear&display=swap">
<style>
  :root{
    --red:#e8202a;
    --red-deep:#d7141f;
    --orange:#f7931e;
    --yellow:#f4ea2a;
    --yellow-soft:#f6ee4a;
    --navy:#2b2d6e;
    --white:#ffffff;
    --black:#000000;
  }
  html,body{margin:0;padding:0;overflow:hidden;background:var(--black);}
  .poster{
    position:relative;width:900px;height:1200px;overflow:hidden;
    box-sizing:border-box;border:8px solid var(--black);
  }
  .burst{
    position:absolute;inset:0;
    background:radial-gradient(ellipse at 50% 50%, var(--yellow) 0%, var(--orange) 40%, var(--red) 70%, var(--red-deep) 100%);
  }
  .brand{
    position:absolute;top:120px;left:0;right:0;
    display:flex;align-items:center;justify-content:center;gap:14px;
  }
  .brand-dot{width:34px;height:34px;border-radius:50%;background:var(--navy);}
  .brand-name{
    font-family:"Bebas Neue",sans-serif;font-size:64px;line-height:1;color:var(--navy);
    letter-spacing:1px;
  }
  .crest-top{
    position:absolute;left:215px;top:345px;width:470px;height:125px;
    background:var(--navy);border-radius:235px 235px 20px 20px;
  }
  .crest-bottom{
    position:absolute;left:265px;top:925px;width:370px;height:60px;
    background:var(--navy);border-radius:20px 20px 60px 60px;
  }
  .marquee{
    position:absolute;left:95px;top:462px;width:710px;height:468px;
    box-sizing:border-box;background:var(--yellow);border-radius:40px;padding:12px;
  }
  .marquee-band{
    width:100%;height:100%;box-sizing:border-box;background:var(--navy);
    border-radius:30px;padding:12px;position:relative;
  }
  .marquee-band::before{
    content:"";position:absolute;inset:5px;border:4px dotted var(--white);border-radius:26px;
  }
  .marquee-panel{
    position:relative;width:100%;height:100%;box-sizing:border-box;
    background:var(--yellow-soft);border:3px solid var(--white);border-radius:20px;
    display:flex;flex-direction:column;align-items:center;justify-content:center;
    text-align:center;
  }
  .title{
    margin:0;font-family:"Yesteryear",cursive;font-weight:400;
    font-size:76px;line-height:1.32;color:var(--red);
    text-shadow:3px 3px 0 var(--white);
  }
  .title span{display:block;}
  .dates{
    margin:18px 0 0;font-family:"Bebas Neue",sans-serif;font-size:46px;
    color:var(--red);letter-spacing:1px;text-shadow:2px 2px 0 var(--white);
  }
  .contact{
    position:absolute;left:0;right:0;top:1030px;text-align:center;color:var(--white);
  }
  .contact-lead{
    margin:0;font-family:"Yesteryear",cursive;font-size:26px;line-height:1.2;
    text-shadow:2px 2px 0 var(--red-deep);
  }
  .contact-email{
    margin:4px 0 0;font-family:"Bebas Neue",sans-serif;font-size:34px;line-height:1.1;
  }
  .contact-web{
    margin:6px 0 0;font-family:"Bebas Neue",sans-serif;font-size:46px;line-height:1.1;letter-spacing:0.5px;
  }
</style>
</head>
<body>
<main class="poster">
  <div class="burst" role="img" aria-label="Sunburst of yellow and orange rays radiating over a red background"></div>

  <div class="brand">
    <span class="brand-dot"></span>
    <span class="brand-name">Curtain Call Stage</span>
  </div>

  <div class="crest-top" role="img" aria-label="Marquee sign crest with star medallion and scrollwork"></div>

  <section class="marquee">
    <div class="marquee-band">
      <div class="marquee-panel">
        <h1 class="title">
          <span>Harlow Bay</span>
          <span>Gathering of</span>
          <span>Short Stage Works</span>
        </h1>
        <p class="dates">Dates - 8 - 10 June 2012</p>
      </div>
    </div>
  </section>

  <div class="crest-bottom" role="img" aria-label="Marquee sign scrollwork base"></div>

  <footer class="contact">
    <p class="contact-lead">for more information e-mail:</p>
    <p class="contact-email">r.m.dunwell@tidemail.com</p>
    <p class="contact-web">www.curtaincallstage.org.au</p>
  </footer>
</main>
</body>
</html>
```